A new website for Electrical Contractor Business

We are looking for a unique and new WordPress website design which would include 5 Pages - Home Page, Meet the Team, Our Services, Our Projects and Contact Us page.

The global theme for the website needs to be professional but simple to navigate as we cater for both business and home owner customers.

Our core business service is targeted around lighting from single room decorative to large office so the theme should incorporate this in some way.

The home page should include;
Our business logo, Contact number, Email address, small Image rotation box - Highlighting pervious projectsText box - With welcome message, chirpnet feed news reel/Customer feed back box.

I would also like to see a 2 boxes for the separate customer types we services. Business and Home Owner. each box will have a small image with a small text description with a link to the area of the services page relevant to that customer type.

Meet the team page -This will be introducing potential customers to the team so I would like it to include for each team member. Something like a small image and text area which will introduce an outline of the team members skills and abilities.

Our Services page This page will be outlining the different services on offer to the both customer types business and homeowner. Each service should have an image with text description of the service would good here.

Our projects page-Will include images of pervious projects and work we have completed along with a text area for the project description/ outliner.

Contact Us page - Should include a contact form which should include an option for the customer to quest us to call them back, also a selection box for them to inform us our how they found our details would be good.

Colour - The theme colours can be taken from the logo or feel free to impress with your own imagination.

Remember we are looking for a website that will interest our customers enough to except our services or be drawn further into the website.. So call to action links to other areas of the site/ contact page are welcome

Target Market(s)

Business - Office, warehousing and Large Store - lighting and Power
Home owner lighting and power

Coding

Coded - Design and coding required

Number of Pages Required

5+ page

Font styles to use
Serif
Sans Serif

Colors

Designer to choose colors to be used in the design.

Requirements
Must have
• Logo integrated into the website design - i.e. website colours which allow the logo to blend into the design.
Nice to have
• Custom but professional theme catering to business customers, but also show that we do provide services to home owners too.
Should not have
• Sorry am not interested in one oversized block image on rotation covering half the home page.. Images will be needed but not a single block over sized frame with not text, shape. Please use your imagination when considering this design

```html
<!DOCTYPE html>
<html lang="en">
<head>
<meta charset="utf-8">
<title>Lumenfield Technologies</title>
<link href="https://fonts.googleapis.com/css2?family=Montserrat:wght@300;400;500;600;700&display=swap" rel="stylesheet">
<style>
:root{
  --orange:#f26b2b;
  --navy:#1e2f66;
  --navy-deep:#172656;
  --card:#2a3d78;
  --text:#5a5f6b;
  --light:#f3f3f3;
  --white:#ffffff;
  --star:#f9c623;
}
*{margin:0;padding:0;box-sizing:border-box}
html,body{width:1200px;height:4042px;overflow:hidden}
body{font-family:'Montserrat',sans-serif;color:var(--text);background:var(--white);position:relative}
.abs{position:absolute}

/* header */
.site-header{position:absolute;top:0;left:0;width:1200px;height:94px;background:var(--white)}
.brand{position:absolute;left:77px;top:24px;display:flex;align-items:center;gap:12px}
.brand-dot{width:48px;height:48px;border-radius:50%;border:5px solid var(--navy)}
.brand-name{font-weight:600;font-size:17px;color:var(--navy);letter-spacing:1px}
.head-contact{position:absolute;top:22px;display:flex;align-items:center;gap:14px}
.head-contact .ring{width:48px;height:48px;border-radius:50%;border:2px solid var(--orange);display:flex;align-items:center;justify-content:center}
.head-contact small{display:block;font-size:12px;color:#777;letter-spacing:.5px}
.head-contact span{font-size:17px;color:#666}

.main-nav{position:absolute;top:94px;left:0;width:1200px;height:52px;background:var(--orange)}
.main-nav ul{list-style:none;position:absolute;left:77px;top:0;display:flex;height:52px}
.main-nav li{font-size:13px;color:var(--white);padding:0 23px;line-height:52px;letter-spacing:.3px}
.main-nav li.active{background:var(--navy);padding:0 20px}
.nav-cta{position:absolute;right:77px;top:0;height:52px;width:166px;background:var(--navy);color:var(--white);font-weight:700;font-size:14px;line-height:52px;text-align:center;letter-spacing:.5px}

/* hero */
.hero{position:absolute;top:146px;left:0;width:1200px;height:552px;background:linear-gradient(160deg,#4a4036 0%,#2d2a24 40%,#1f2220 70%,#3b3934 100%)}
.hero h1{position:absolute;top:200px;width:100%;text-align:center;color:var(--white);font-weight:700;font-size:38px;letter-spacing:.5px}
.hero p{position:absolute;top:262px;width:100%;text-align:center;color:var(--white);font-size:19px;line-height:31px;font-weight:400}
.hero-tab{position:absolute;top:655px;left:315px;width:570px;height:90px;background:var(--white);clip-path:polygon(8% 0,92% 0,100% 50%,100% 100%,0 100%,0 50%)}
.hero-pill{position:absolute;top:667px;left:323px;height:64px;display:flex}
.pill{height:64px;display:flex;align-items:center;gap:16px;color:var(--white);font-size:15px;padding:0 0 0 56px}
.pill.phone{width:240px;background:var(--orange);clip-path:polygon(20px 0,100% 0,100% 100%,20px 100%,0 50%)}
.pill.mail{width:312px;background:var(--navy);padding-left:42px;clip-path:polygon(0 0,calc(100% - 30px) 0,100% 50%,calc(100% - 30px) 100%,0 100%)}

/* welcome */
.welcome h2{position:absolute;left:79px;top:800px;font-size:33px;font-weight:700;color:var(--navy);line-height:49px;letter-spacing:.5px}
.welcome h2 em{font-style:normal;color:var(--orange)}
.welcome .lead{position:absolute;left:79px;top:920px;width:620px;font-size:13px;line-height:25px}
.welcome .mark{position:absolute;left:77px;top:1025px;width:186px;height:186px;border-radius:50%;border:9px solid var(--navy);display:flex;align-items:center;justify-content:center;font-weight:700;font-size:48px;color:var(--orange)}
.welcome .side{position:absolute;left:328px;top:1024px;width:370px;font-size:13px;line-height:25px}
.quote{position:absolute;left:769px;top:805px;width:354px;height:395px;border:1px solid #d5d5d5;border-radius:4px;background:var(--white)}
.quote-head{height:84px;background:var(--navy);clip-path:polygon(0 0,100% 0,100% 72%,50% 100%,0 72%);color:var(--white);font-weight:700;font-size:22px;text-align:center;padding-top:20px;letter-spacing:.5px}
.field{position:absolute;left:26px;width:302px;height:40px;background:var(--light);border:1px solid #cfcfcf;font-size:13px;color:#777;padding:12px 17px}
.send{position:absolute;left:26px;top:318px;width:302px;height:42px;background:var(--navy);color:var(--white);font-weight:700;font-size:17px;text-align:center;line-height:42px}

/* services */
.svc{position:absolute;left:0;width:1200px}
.svc-home{top:1282px;height:436px;background:linear-gradient(120deg,#2a3f7a 0%,#223570 45%,#1e2f66 100%)}
.svc-office{top:1718px;height:395px;background:linear-gradient(180deg,#e9ebf2 0%,#f4f5f8 45%,#e3e1df 100%)}
.svc h2{position:absolute;top:50px;width:100%;text-align:center;color:var(--orange);font-size:33px;font-weight:700}
.icon-disc{position:absolute;width:230px;height:230px;border-radius:50%;background:var(--white);display:flex;align-items:center;justify-content:center}
.icon-disc div{width:208px;height:208px;border-radius:50%;background:var(--orange);display:flex;align-items:center;justify-content:center}
.svc h3{position:absolute;font-size:28px;font-weight:600}
.svc p{position:absolute;width:590px;font-size:12.5px;line-height:25px}
.svc-home h3,.svc-home p{color:var(--white)}
.svc-office h3{color:var(--navy)}
.svc-office p{color:#333}

/* gallery */
.section-title{position:absolute;width:100%;left:0;text-align:center;font-size:33px;font-weight:700;color:var(--navy);letter-spacing:.5px}
.section-title em{font-style:normal;color:var(--orange)}
.gallery{position:absolute;top:2233px;left:77px;width:1046px;display:grid;grid-template-columns:repeat(4,240px);column-gap:28.6px;row-gap:33px}
.gallery div{height:165px}

/* testimonials */
.testimonials{position:absolute;top:2677px;left:0;width:1200px;height:604px;background:var(--navy)}
.card{position:absolute;top:119px;width:323px;background:var(--card);padding:40px 22px 0 22px;color:var(--white);font-size:13px;line-height:25px}
.card .who{margin-top:18px;font-size:13px;display:flex;align-items:center;gap:14px}

/* blog */
.post{position:absolute;top:3400px;display:flex;gap:29px}
.post .thumb{width:209px;height:155px}
.post small{display:block;font-size:12px;margin-top:14px;color:#666}
.post h4{font-weight:500;font-size:16px;color:var(--navy);margin-top:14px}
.post .rule{width:28px;height:2px;background:var(--orange);margin:14px 0 10px}
.post p{font-size:12.5px;line-height:25px;width:260px;color:#777}

/* footer */
.site-footer{position:absolute;top:3635px;left:0;width:1200px;height:347px;background:var(--navy);color:var(--white)}
.site-footer h5{position:absolute;top:65px;color:var(--orange);font-size:18px;font-weight:600;letter-spacing:.5px}
.f-item{position:absolute;display:flex;gap:18px;font-size:13px;line-height:25px}
.f-item time{display:block;color:var(--orange);font-size:12px}
.copyright{position:absolute;top:3982px;left:0;width:1200px;height:60px;background:var(--orange);color:var(--white);font-size:13px;text-align:center;line-height:60px}
</style>
</head>
<body>

<svg width="0" height="0" style="position:absolute">
  <defs><path id="st" d="M8 0l2.4 5 5.6.6-4.2 3.8 1.2 5.6L8 12.2 3 15l1.2-5.6L0 5.6 5.6 5z"/></defs>
</svg>

<header class="site-header">
  <div class="brand"><div class="brand-dot"></div><div class="brand-name">LUMENFIELD</div></div>
  <div class="head-contact" style="left:611px">
    <div class="ring"><svg width="18" height="14" viewBox="0 0 18 14"><rect width="18" height="14" rx="2" fill="#1e2f66"/><path d="M1 2l8 6 8-6" stroke="#fff" stroke-width="1.6" fill="none"/></svg></div>
    <div><small>EMAIL US ON</small><span>info@lumenfield-tech.com</span></div>
  </div>
  <div class="head-contact" style="left:916px">
    <div class="ring"><svg width="18" height="18" viewBox="0 0 24 24"><path fill="#1e2f66" d="M6.6 10.8a15 15 0 006.6 6.6l2.2-2.2c.3-.3.7-.4 1-.2 1.1.4 2.3.6 3.6.6.6 0 1 .4 1 1V20c0 .6-.4 1-1 1A17 17 0 013 4c0-.6.4-1 1-1h3.5c.6 0 1 .4 1 1 0 1.2.2 2.4.6 3.6.1.3 0 .7-.2 1z"/></svg></div>
    <div><small>CALL US ON</small><span>123 456 7890</span></div>
  </div>
</header>

<nav class="main-nav">
  <ul>
    <li class="active">HOME</li><li>MEET THE TEAM</li><li>OUR SERVICES</li><li>PROJECTS</li><li>CONTACT</li>
  </ul>
  <div class="nav-cta">GET IN TOUCH</div>
</nav>

<section class="hero" role="img" aria-label="Dark modern office lobby with round ceiling lights, tall columns, palms and black lounge chairs">
  <h1>LUMENFIELD TECHNOLOGIES.</h1>
  <p>Lorem Ipsum is simply dummy text of the printing and typesetting industry.<br>Lorem Ipsum has been the industry's standard dummy text ever.</p>
</section>
<div class="hero-tab"></div>
<div class="hero-pill">
  <div class="pill phone"><svg width="20" height="20" viewBox="0 0 24 24"><path fill="#fff" d="M6.6 10.8a15 15 0 006.6 6.6l2.2-2.2c.3-.3.7-.4 1-.2 1.1.4 2.3.6 3.6.6.6 0 1 .4 1 1V20c0 .6-.4 1-1 1A17 17 0 013 4c0-.6.4-1 1-1h3.5c.6 0 1 .4 1 1 0 1.2.2 2.4.6 3.6.1.3 0 .7-.2 1z"/></svg>123 456 7890</div>
  <div class="pill mail"><svg width="18" height="14" viewBox="0 0 18 14"><rect width="18" height="14" rx="2" fill="#fff"/><path d="M1 2l8 6 8-6" stroke="#1e2f66" stroke-width="1.6" fill="none"/></svg>info@lumenfield-tech.com</div>
</div>

<section class="welcome">
  <h2><em>WELCOME TO</em> LUMENFIELD<br>TECHNOLOGIES</h2>
  <p class="lead">Lorem Ipsum is simply dummy text of the printing and typesetting industry. Lorem Ipsum has been the industry's standard dummy text ever since the 1500s, when an unknown printer took a galley of type and scrambled it to make a type specimen book.</p>
  <div class="mark">LF</div>
  <p class="side">It has survived not only five centuries, but also the leap into electronic typesetting, remaining essentially unchanged. It was popularised in the 1960s with the release of Pressline sheets containing Lorem Ipsum passages, and more recently with desktop publishing software like Pagecraft Studio including versions of Lorem Ipsum.</p>
  <form class="quote">
    <div class="quote-head">GET FREE QUOTE</div>
    <div class="field" style="top:110px">Name</div>
    <div class="field" style="top:162px">Email</div>
    <div class="field" style="top:215px;height:93px">Message</div>
    <div class="send">SEND</div>
  </form>
</section>

<section class="svc svc-home">
  <h2>OUR SERVICES</h2>
  <div class="icon-disc" style="left:142px;top:126px"><div>
    <svg width="112" height="104" viewBox="0 0 112 104"><path d="M56 4L4 50h14v50h28V72h20v28h28V50h14z" fill="#fff"/><rect x="78" y="12" width="14" height="24" fill="#fff"/></svg>
  </div></div>
  <h3 style="left:485px;top:140px">Room decorative lighting</h3>
  <p style="left:485px;top:196px">Lorem Ipsum is simply dummy text of the printing and typesetting industry. Lorem Ipsum has been the industry's standard dummy text ever since the 1500s, when an unknown printer took a galley of type and scrambled it to make a type specimen book. It has survived not only five centuries, but also the leap into electronic typesetting, remaining essentially unchanged. It was popularised in the 1960s with the release of Pressline.</p>
</section>

<section class="svc svc-office">
  <h3 style="left:156px;top:110px">Office decorative lighting</h3>
  <p style="left:156px;top:166px">Lorem Ipsum is simply dummy text of the printing and typesetting industry. Lorem Ipsum has been the industry's standard dummy text ever since the 1500s, when an unknown printer took a galley of type and scrambled it to make a type specimen book. It has survived not only five centuries, but also the leap into electronic typesetting, remaining essentially unchanged. It was popularised in the 1960s with the release of Pressline.</p>
  <div class="icon-disc" style="left:810px;top:85px"><div>
    <svg width="80" height="110" viewBox="0 0 80 110"><rect x="18" y="4" width="44" height="46" rx="12" fill="#fff"/><rect x="8" y="54" width="64" height="14" rx="5" fill="#fff"/><rect x="0" y="36" width="8" height="26" rx="3" fill="#fff"/><rect x="72" y="36" width="8" height="26" rx="3" fill="#fff"/><rect x="36" y="68" width="8" height="20" fill="#fff"/><path d="M8 96l32-10 32 10" stroke="#fff" stroke-width="6" fill="none" stroke-linecap="round"/><circle cx="8" cy="102" r="5" fill="#fff"/><circle cx="72" cy="102" r="5" fill="#fff"/><circle cx="40" cy="100" r="5" fill="#fff"/></svg>
  </div></div>
</section>

<h2 class="section-title" style="top:2162px"><em>PROJECT</em> GALLERY</h2>
<div class="gallery">
  <div role="img" aria-label="Living room with white sofa and brick wall" style="background:linear-gradient(135deg,#3b3632,#7d6f62 60%,#d9d4cf)"></div>
  <div role="img" aria-label="Dining room with pendant lamps" style="background:linear-gradient(135deg,#f1ede8,#8a7d74 55%,#3c3431)"></div>
  <div role="img" aria-label="Bedroom with warm wood ceiling" style="background:linear-gradient(135deg,#6a4a30,#b28461 50%,#e9e2da)"></div>
  <div role="img" aria-label="Bright office lounge with cove lighting" style="background:linear-gradient(135deg,#e8e9ea,#c4c8cc 55%,#8f8a86)"></div>
  <div role="img" aria-label="Light grey living room with staircase" style="background:linear-gradient(135deg,#d9d6d2,#b8b3ad 55%,#8f96a0)"></div>
  <div role="img" aria-label="Open plan room with wooden floor" style="background:linear-gradient(135deg,#a98f78,#6e4c33 55%,#3a2a20)"></div>
  <div role="img" aria-label="Reception desk under round ceiling lights" style="background:linear-gradient(180deg,#f4f3f1,#c9b8a4 55%,#403c3a)"></div>
  <div role="img" aria-label="Hotel bedroom with warm lamps" style="background:linear-gradient(135deg,#3a2b20,#8c5e36 50%,#e6c79e)"></div>
</div>

<section class="testimonials">
  <h2 class="section-title" style="top:48px;color:#fff">CLIENT TESTIMONIALS</h2>
  <div class="card" style="left:77px;height:334px">Lorem Ipsum is simply dummy text of the printing and typesetting industry. Lorem Ipsum has been the industry's standard dummy text ever since the 1500s, when an unknown printer took a galley of type and scrambled it to make a type specimen book. It has survived not only five centurie but also the leap into electronic.
    <div class="who">- NAME SURNAME <svg width="88" height="16" viewBox="0 0 88 16"><g fill="#f9c623"><use href="#st"/><use href="#st" x="18"/><use href="#st" x="36"/><use href="#st" x="54"/><use href="#st" x="72"/></g></svg></div></div>
  <div class="card" style="left:438px;height:386px">Lorem Ipsum is simply dummy text of the printing and typesetting industry. Lorem Ipsum has been the industry's standard dummy text ever since the 1500s, when an unknown printer took a galley of type and scrambled it to make a type specimen book. It has survived not only five centurie, but also the leap into electronic typesetting, remaining essentially unchang. It was popularised in the 1960s with the.
    <div class="who">- NAME SURNAME <svg width="88" height="16" viewBox="0 0 88 16"><g fill="#f9c623"><use href="#st"/><use href="#st" x="18"/><use href="#st" x="36"/><use href="#st" x="54"/><use href="#st" x="72"/></g></svg></div></div>
  <div class="card" style="left:800px;height:334px">Lorem Ipsum is simply dummy text of the printing and typesetting industry. Lorem Ipsum has been the industry's standard dummy text ever since the 1500s, when an unknown printer took a galley of type and scrambled it to make a type specimen book. It has survived not only five centurie but also the leap into electronic.
    <div class="who">- NAME SURNAME <svg width="88" height="16" viewBox="0 0 88 16"><g fill="#f9c623"><use href="#st"/><use href="#st" x="18"/><use href="#st" x="36"/><use href="#st" x="54"/><use href="#st" x="72"/></g></svg></div></div>
</section>

<h2 class="section-title" style="top:3330px"><em>BLOG</em> POST</h2>
<article class="post" style="left:77px">
  <div class="thumb" role="img" aria-label="Dark lounge with shelving and warm lighting" style="background:linear-gradient(135deg,#1f1c1a,#6b5440 55%,#c9a57c)"></div>
  <div><small>20 JUN 2019</small><h4>Lorem Ipsum is simply dummy.</h4><div class="rule"></div><p>Lorem Ipsum is simply dummy text of the printing and typesetting industry Lorem Ipsum has been.</p></div>
</article>
<article class="post" style="left:623px">
  <div class="thumb" role="img" aria-label="Bright open office with rows of desks and blue chairs" style="background:linear-gradient(180deg,#f2f4f6,#cfd6de 55%,#3b4a6b)"></div>
  <div><small>20 JUN 2019</small><h4>Lorem Ipsum is simply dummy.</h4><div class="rule"></div><p>Lorem Ipsum is simply dummy text of the printing and typesetting industry Lorem Ipsum has been.</p></div>
</article>

<footer class="site-footer">
  <div class="abs" style="left:77px;top:50px;display:flex;align-items:center;gap:12px"><div style="width:64px;height:64px;border-radius:50%;border:5px solid #fff"></div><div style="font-size:19px;font-weight:500;letter-spacing:1px">LUMENFIELD</div></div>
  <p class="abs" style="left:79px;top:146px;width:280px;font-size:13px;line-height:25px">Lorem Ipsum is simply dummy text of the printing and typesetting industry. Lorem Ipsum has been the industry's standard.</p>

  <h5 style="left:441px">RECENT CHIRPNET POSTS</h5>
  <div class="f-item" style="left:441px;top:108px"><div style="width:24px;height:24px;border-radius:50%;background:#fff;margin-top:4px;flex:none"></div><div style="width:250px">Lorem Ipsum is simply dummy text of the printing and typesetting industry.<time>4 days ago</time></div></div>
  <div class="f-item" style="left:441px;top:207px"><div style="width:24px;height:24px;border-radius:50%;background:#fff;margin-top:4px;flex:none"></div><div style="width:250px">Lorem Ipsum is simply dummy text of the printing and typesetting industry.<time>4 days ago</time></div></div>

  <h5 style="left:802px">CONTACT INFO</h5>
  <div class="f-item" style="left:802px;top:108px"><svg width="18" height="24" viewBox="0 0 18 24" style="flex:none;margin-top:4px"><path d="M9 0a9 9 0 00-9 9c0 7 9 15 9 15s9-8 9-15a9 9 0 00-9-9z" fill="#f26b2b"/><circle cx="9" cy="9" r="3.5" fill="#1e2f66"/></svg><div style="width:260px">Lorem Ipsum is simply dummy text of the printing and typesetting industry.</div></div>
  <div class="f-item" style="left:802px;top:172px"><svg width="18" height="18" viewBox="0 0 24 24" style="flex:none;margin-top:3px"><path fill="#f26b2b" d="M6.6 10.8a15 15 0 006.6 6.6l2.2-2.2c.3-.3.7-.4 1-.2 1.1.4 2.3.6 3.6.6.6 0 1 .4 1 1V20c0 .6-.4 1-1 1A17 17 0 013 4c0-.6.4-1 1-1h3.5c.6 0 1 .4 1 1 0 1.2.2 2.4.6 3.6.1.3 0 .7-.2 1z"/></svg>123 456 7890</div>
  <div class="f-item" style="left:802px;top:210px"><svg width="18" height="14" viewBox="0 0 18 14" style="flex:none;margin-top:6px"><rect width="18" height="14" rx="2" fill="#f26b2b"/><path d="M1 2l8 6 8-6" stroke="#1e2f66" stroke-width="1.6" fill="none"/></svg>info@lumenfield-tech.com</div>
</footer>
<div class="copyright">©LUMENFIELD TECHNOLOGIES- 2019. All Rights Reserved.</div>

</body>
</html>
```